Orthopaedic Clinic Needs facebook page

Orthopaedic Clinic needs facebook page. The name of our clinic is Larchmont Orthopaedics. We focus on hip and knee orthopaedic conditions, as well as general orthopaedics. The main services are total knee replacements, total hip replacements, sports injury of the knee, hip fractures. Unique selling points of our service would be 1. Patient Centred Care, 2. Value Driven, 3. 2 Double-Fellowship Trained Surgeons.

Colour scheme should fit the logo design and be within the general colour recommendations of a medical clinic.

The design should be modern, eye catching, draws the end user to the website.

We would like to design our facebook page for future social media marketing.
In accordance with local advertisement regulations pertaining to medical clinics, no statements must have any information or laudatory statements such as the use of best, better, breakthrough, champions, or any statements that imply superiority and that may create unjustified expectations of services.

Target Market(s)

Patients
Friends family and relatives of patients.

Font styles to use
Serif
Sans Serif

Requirements
Must have
• My project must have my logo.

A nice colour scheme comfortable to the eye.
Nice to have
• Nice eye catching design that will draw the end user to the page.
Should not have
• Must not have any information that create unjustified expectaions.
Must not contain laudatory statements such as best, better, breakthrough, champions, or other statement that may create unjustified expecation of services.

```html
<!DOCTYPE html>
<html lang="en">
<head>
<meta charset="utf-8">
<title>Larchmont Orthopaedics – Page</title>
<link rel="stylesheet" href="https://fonts.googleapis.com/css2?family=Arimo:wght@400;700&family=Montserrat:wght@300;400&display=swap">
<style>
  :root{
    --fb-blue:#4267b2;
    --page-bg:#e9ebee;
    --card:#ffffff;
    --border:#dddfe2;
    --ink:#1c1e21;
    --muted:#606770;
    --link:#385898;
    --teal-deep:#0b3236;
    --teal:#1e8a7a;
    --teal-soft:#4fb3a5;
    --green:#42b72a;
  }
  *{box-sizing:border-box;margin:0;padding:0}
  html,body{width:1200px;height:800px;overflow:hidden}
  body{background:var(--page-bg);font-family:"Arimo",Arial,sans-serif;color:var(--ink);position:relative}

  .topbar{position:absolute;left:0;top:0;width:1200px;height:45px;background:var(--fb-blue);border-bottom:1px solid #29487d}
  .topbar .site-mark{position:absolute;left:29px;top:8px;width:27px;height:27px;background:#fff;border-radius:3px}
  .topbar .search{position:absolute;left:65px;top:7px;width:504px;height:28px;background:#fff;border-radius:3px}
  .topbar .search svg{position:absolute;right:10px;top:6px}
  .topbar .avatar{position:absolute;left:586px;top:8px;width:28px;height:28px;border-radius:50%;background:#2a2a2a}
  .topbar .nav{position:absolute;left:669px;top:0;height:45px;display:flex;align-items:center;gap:0}
  .topbar .nav a{color:#fff;font-weight:700;font-size:14px;text-decoration:none;padding:0 14px;border-left:1px solid rgba(0,0,0,.15);line-height:20px}
  .topbar .icons{position:absolute;left:925px;top:10px;display:flex;gap:20px}
  .topbar .badge{position:absolute;left:978px;top:5px;background:#fa3e3e;color:#fff;font-size:10px;font-weight:700;border-radius:3px;padding:0 3px;line-height:13px}

  .sidebar{position:absolute;left:0;top:45px;width:246px}
  .profile-disc{position:absolute;left:30px;top:13px;width:204px;height:204px;border-radius:50%;background:#fff;display:flex;align-items:center;justify-content:center;gap:8px}
  .profile-disc .mark{width:30px;height:30px;background:var(--teal-soft)}
  .profile-disc .wordmark{font-family:"Montserrat",sans-serif;font-weight:300;color:#4a6b70;line-height:1}
  .profile-disc .wordmark .l1{font-size:15px;letter-spacing:.5px;display:block}
  .profile-disc .wordmark .l2{font-size:9px;letter-spacing:2.3px;display:block;margin-top:3px}
  .page-name{position:absolute;left:30px;top:233px;font-size:22px;line-height:24px;font-weight:400}
  .page-handle{position:absolute;left:31px;top:284px;font-size:15px;font-weight:700;color:var(--muted)}
  .menu{position:absolute;left:25px;top:318px;width:209px;list-style:none}
  .menu li{height:36px;line-height:36px;padding-left:10px;font-size:16px;color:#1d2129}
  .menu li.active{background:#f5f6f7;border:1px solid var(--border);font-weight:700}
  .create-page{position:absolute;left:30px;top:581px;width:110px;height:26px;background:var(--green);color:#fff;font-weight:700;font-size:13px;line-height:26px;text-align:center;border-radius:2px;border:1px solid #36a420}

  .cover{position:absolute;left:246px;top:45px;width:928px;height:355px;background:var(--teal-deep);overflow:hidden}
  .cover svg.photos{position:absolute;left:0;top:0}
  .brand{position:absolute;left:232px;top:17px;display:flex;align-items:center;gap:22px}
  .brand .mark{width:86px;height:86px;background:var(--teal)}
  .brand .wordmark{font-family:"Montserrat",sans-serif;font-weight:300;color:#fff;line-height:1}
  .brand .l1{display:block;font-size:45px;letter-spacing:1px}
  .brand .l2{display:block;font-size:25px;letter-spacing:7.4px;margin-top:10px}
  .usp{position:absolute;color:#fff;font-size:18px;line-height:22px;text-align:right;font-weight:400}
  .usp::after{content:"";position:absolute;right:-9px;top:-32px;width:2px;height:72px;background:var(--teal)}
  .usp.care{right:641px;top:164px}
  .usp.value{right:364px;top:164px}
  .usp.surgeons{right:125px;top:153px}
  .usp.surgeons::after{top:-20px}

  .action-bar{position:absolute;left:246px;top:400px;width:928px;height:57px;background:var(--card);border:1px solid var(--border);border-top:none}
  .actions{position:absolute;left:15px;top:11px;display:flex;border:1px solid #ccd0d5;border-radius:2px;background:#f5f6f7}
  .actions span{display:flex;align-items:center;gap:6px;height:29px;padding:0 12px;font-size:14px;font-weight:700;color:#4b4f56;border-left:1px solid #ccd0d5}
  .actions span:first-child{border-left:none}
  .send{position:absolute;left:588px;top:11px;width:325px;height:30px;background:var(--fb-blue);border:1px solid #365899;border-radius:2px;color:#fff;font-size:16px;display:flex;align-items:center;justify-content:center;gap:8px}

  .content-card{position:absolute;left:246px;top:472px;width:928px;height:340px;background:var(--card);border:1px solid var(--border);border-radius:3px}
  .suggest{position:absolute;right:28px;top:21px;color:#1c6fe0;font-size:14px;font-weight:700;display:flex;align-items:center;gap:8px}
</style>
</head>
<body>

<header class="topbar">
  <div class="site-mark"></div>
  <div class="search">
    <svg width="16" height="16" viewBox="0 0 16 16"><circle cx="6.5" cy="6.5" r="5" fill="none" stroke="#1d2129" stroke-width="1.8"/><line x1="10.2" y1="10.2" x2="15" y2="15" stroke="#1d2129" stroke-width="1.8"/></svg>
  </div>
  <div class="avatar"></div>
  <nav class="nav"><a>Home</a><a>Find Friends</a><a>Create</a></nav>
  <div class="icons">
    <svg width="24" height="22" viewBox="0 0 24 22"><circle cx="8" cy="6" r="4" fill="#1d2d50"/><path d="M0 19c0-5 4-7 8-7s8 2 8 7z" fill="#1d2d50"/><circle cx="16" cy="5" r="3.5" fill="#1d2d50"/><path d="M14 11c5 0 10 2 10 7h-6" fill="#1d2d50"/></svg>
    <svg width="22" height="22" viewBox="0 0 22 22"><circle cx="11" cy="10" r="10" fill="#fff"/></svg>
    <svg width="20" height="22" viewBox="0 0 20 22"><path d="M10 1c4 0 6 3 6 7v5l3 4H1l3-4V8c0-4 2-7 6-7z" fill="#1d2d50"/><circle cx="10" cy="19.5" r="2.2" fill="#1d2d50"/></svg>
    <svg width="26" height="22" viewBox="0 0 26 22"><circle cx="7" cy="6" r="4" fill="#1d2d50"/><path d="M0 20c0-5 3-7 7-7s7 2 7 7z" fill="#1d2d50"/><rect x="15" y="9" width="10" height="11" fill="#1d2d50"/></svg>
    <svg width="22" height="22" viewBox="0 0 22 22"><circle cx="11" cy="11" r="11" fill="#1d2d50"/><text x="11" y="16" font-size="14" font-weight="700" fill="#fff" text-anchor="middle" font-family="Arimo,sans-serif">?</text></svg>
    <svg width="14" height="22" viewBox="0 0 14 22"><path d="M1 9h12l-6 7z" fill="#1d2d50"/></svg>
  </div>
  <div class="badge">1</div>
</header>

<aside class="sidebar">
  <div class="profile-disc">
    <div class="mark"></div>
    <div class="wordmark"><span class="l1">LARCHMONT</span><span class="l2">ORTHOPAEDICS</span></div>
  </div>
  <h1 class="page-name">Larchmont<br>Orthopaedics</h1>
  <div class="page-handle">@LarchmontOrthopaedics</div>
  <ul class="menu">
    <li>Home</li><li>Services</li><li>Reviews</li><li>Photos</li><li>Posts</li>
    <li class="active">About</li><li>Community</li>
  </ul>
  <div class="create-page">Create a Page</div>
</aside>

<section class="cover">
  <svg class="photos" width="928" height="355" viewBox="0 0 928 355">
    <defs>
      <linearGradient id="careTone" x1="0" y1="0" x2="1" y2="1">
        <stop offset="0" stop-color="#6b5a46"/><stop offset=".6" stop-color="#a98c6e"/><stop offset="1" stop-color="#c9c2b4"/>
      </linearGradient>
      <linearGradient id="valueTone" x1="0" y1="0" x2="1" y2="1">
        <stop offset="0" stop-color="#3b4447"/><stop offset=".5" stop-color="#8a6a52"/><stop offset="1" stop-color="#d9dcdc"/>
      </linearGradient>
      <linearGradient id="surgeryTone" x1="0" y1="0" x2="1" y2="1">
        <stop offset="0" stop-color="#5a6460"/><stop offset=".5" stop-color="#d8c9a6"/><stop offset="1" stop-color="#b8ab8c"/>
      </linearGradient>
      <linearGradient id="fadeTop" x1="0" y1="0" x2="0" y2="1">
        <stop offset="0" stop-color="#0b3236" stop-opacity="1"/><stop offset=".42" stop-color="#0b3236" stop-opacity=".95"/><stop offset=".75" stop-color="#0b3236" stop-opacity=".2"/><stop offset="1" stop-color="#0b3236" stop-opacity="0"/>
      </linearGradient>
    </defs>
    <polygon role="img" aria-label="Photo of a caring hand resting on an elderly patient's shoulder" points="0,120 338,120 290,355 0,355" fill="url(#careTone)"/>
    <polygon role="img" aria-label="Photo of a doctor's hand reviewing an X-ray" points="346,120 618,120 566,355 298,355" fill="url(#valueTone)"/>
    <polygon role="img" aria-label="Photo of gloved surgeons' hands operating" points="626,120 928,120 928,355 574,355" fill="url(#surgeryTone)"/>
    <rect x="0" y="0" width="928" height="355" fill="url(#fadeTop)"/>
  </svg>
  <div class="brand">
    <div class="mark"></div>
    <div class="wordmark"><span class="l1">LARCHMONT</span><span class="l2">ORTHOPAEDICS</span></div>
  </div>
  <p class="usp care">Patient Centred Care</p>
  <p class="usp value">Value Driven</p>
  <p class="usp surgeons">2 Double-Fellowship<br>Trained Surgeons</p>
</section>

<div class="action-bar">
  <div class="actions">
    <span><svg width="16" height="16" viewBox="0 0 16 16"><circle cx="3" cy="13" r="2" fill="#4b4f56"/><path d="M1 7a8 8 0 0 1 8 8M1 2a13 13 0 0 1 13 13" fill="none" stroke="#4b4f56" stroke-width="1.8"/></svg>Follow</span>
    <span><svg width="16" height="14" viewBox="0 0 16 14"><path d="M9 1l7 6-7 6V9C4 9 2 11 0 13c1-5 4-8 9-8z" fill="#4b4f56"/></svg>Share</span>
    <span><svg width="12" height="15" viewBox="0 0 12 15"><path d="M1 1h10v13l-5-4-5 4z" fill="#4b4f56"/></svg>Save</span>
    <span>···</span>
  </div>
  <div class="send"><svg width="18" height="18" viewBox="0 0 18 18"><circle cx="9" cy="9" r="8" fill="none" stroke="#fff" stroke-width="1.6"/></svg>Send Message</div>
</div>

<main class="content-card">
  <div class="suggest"><svg width="14" height="14" viewBox="0 0 14 14"><path d="M1 13l1-4 8-8 3 3-8 8z" fill="#1c6fe0"/></svg>Suggest Edits</div>
</main>

</body>
</html>
```